Stationery Design Project

QV7 Staffing requires letterhead and business card designs for a company based in London. Just like the name, we're a management resourcing company, providing resources to third party companies. You can see www.qv7staffing-example.com for ideas on existing colour schemes and design concepts that have been implimented and agreed to. Ultimately the design should broadcast professionalism, safety and the concept of growth.

Target Market(s)

Financial institutes; friendly societies (All UK based)

Industry/Entity Type

Safety

Requirements
Must have
• Files produced should be print ready; and the text in them editable (eg address, name etc)

```html
<!DOCTYPE html>
<html lang="en">
<head>
<meta charset="utf-8">
<title>QV7 Staffing — Letterhead</title>
<link rel="stylesheet" href="https://fonts.googleapis.com/css2?family=Open+Sans:wght@400;600;700&display=swap">
<style>
  :root {
    --teal: #2ba3b6;
    --teal-deep: #1c8ea2;
    --sky-wash: #e3f0f8;
    --paper: #ffffff;
    --rule: #9fd3de;
  }
  * { margin: 0; padding: 0; box-sizing: border-box; }
  html, body {
    width: 848px;
    height: 1200px;
    overflow: hidden;
    background: var(--paper);
  }
  .letterhead {
    position: relative;
    width: 848px;
    height: 1200px;
    overflow: hidden;
    font-family: "Open Sans", Arial, sans-serif;
    background:
      linear-gradient(to bottom, var(--sky-wash) 0%, rgba(227,240,248,0) 28%),
      linear-gradient(to top, var(--sky-wash) 0%, rgba(227,240,248,0) 9%),
      var(--paper);
  }
  .brand {
    position: absolute;
    left: 70px;
    top: 52px;
    display: flex;
    align-items: center;
    gap: 10px;
  }
  .brand-mark {
    width: 18px;
    height: 18px;
    background: var(--teal);
  }
  .brand-name {
    font-size: 28px;
    font-weight: 700;
    letter-spacing: -0.3px;
    color: var(--teal);
    line-height: 1;
  }
  .header-rule {
    position: absolute;
    left: 0;
    top: 114px;
    width: 62px;
    height: 2px;
    background: var(--rule);
  }
  .contact {
    position: absolute;
    left: 63px;
    top: 136px;
    font-size: 11px;
    color: var(--teal);
    font-style: normal;
  }
  .contact-line {
    display: block;
    height: 14px;
    line-height: 14px;
    white-space: nowrap;
  }
  .contact-label {
    font-size: 7px;
    line-height: 1;
    text-transform: uppercase;
    letter-spacing: 0.4px;
    color: var(--teal-deep);
    margin-right: 3px;
  }
  .contact-gap { margin-left: 8px; }
</style>
</head>
<body>
  <main class="letterhead">
    <header class="brand">
      <span class="brand-mark" aria-hidden="true"></span>
      <span class="brand-name">QV7 Staffing</span>
    </header>
    <div class="header-rule" aria-hidden="true"></div>
    <address class="contact">
      <span class="contact-line">Address Address Address</span>
      <span class="contact-line">Postal Code England</span>
      <span class="contact-line"><span class="contact-label">Phone</span>020 7946 0018<span class="contact-gap"><span class="contact-label">Fax</span>020 7946 0019</span></span>
      <span class="contact-line"><span class="contact-label">Email</span>name@qv7staffing-example.com</span>
      <span class="contact-line"><span class="contact-label">Web</span>www.qv7staffing-example.com</span>
    </address>
  </main>
</body>
</html>
```